Velvet Dare Age Verification Landing Page

To create a visually appealing design for the landing page of the adult game "Velvet Dare" that confirms the visitor's age.
The design should have a simple and visually appealing look that focuses on two buttons labeled "Yes" and "No". The purpose of the page is to confirm that the visitor is 18 years of age or older before accessing the game's content. Responsive design that works well on desktop and mobile devices. The final output should be delivered in PSD, AI, or Sketch format, along with any necessary images or assets.
I have also attached examples.

```html
<!DOCTYPE html>
<html lang="en">
<head>
<meta charset="UTF-8">
<title>Velvet Dare – Age Verification</title>
<link rel="stylesheet" href="https://fonts.googleapis.com/css2?family=Playfair+Display:wght@400;700&display=swap">
<style>
  :root {
    --bg-light: #d2b0d2;
    --bg-mid: #a577a8;
    --bg-dark: #5e3460;
    --panel: rgba(58, 32, 50, 0.82);
    --frame: #ffffff;
    --text: #ffffff;
    --accent: #a474b1;
    --accent-line: #b96fb4;
  }
  * { margin: 0; padding: 0; box-sizing: border-box; }
  html, body { width: 1200px; height: 557px; overflow: hidden; }
  body { font-family: "Playfair Display", Georgia, serif; color: var(--text); }

  .page { position: relative; width: 1200px; height: 557px; overflow: hidden; }

  .hero-photo {
    position: absolute; inset: 0;
    background:
      radial-gradient(ellipse 45% 60% at 80% 45%, rgba(70, 35, 70, 0.55), transparent 70%),
      radial-gradient(ellipse 40% 50% at 20% 40%, rgba(230, 200, 230, 0.5), transparent 70%),
      linear-gradient(100deg, var(--bg-light) 0%, var(--bg-mid) 45%, var(--bg-dark) 100%);
  }

  .dialog-panel {
    position: absolute; left: 334px; top: 131px; width: 532px; height: 291px;
    background: var(--panel); border-radius: 26px; transform: rotate(-2deg);
  }
  .dialog-frame {
    position: absolute; left: 340px; top: 134px; width: 516px; height: 291px;
    border: 2px solid var(--frame); border-radius: 26px; transform: rotate(2.6deg);
  }

  .dialog {
    position: absolute; left: 334px; top: 0; width: 532px; height: 557px;
    text-align: center;
  }
  .brand {
    position: absolute; top: 176px; left: 0; right: 0;
    display: flex; align-items: center; justify-content: center; gap: 10px;
    font-size: 27px; font-weight: 700;
  }
  .brand-dot { width: 14px; height: 14px; border-radius: 50%; background: var(--text); }

  .question {
    position: absolute; top: 252px; left: 0; right: 0;
    font-size: 26px; font-weight: 700; letter-spacing: -0.2px;
  }

  .choices {
    position: absolute; top: 298px; left: 0; right: 0;
    display: flex; justify-content: center; gap: 21px;
  }
  .choice {
    width: 103px; height: 42px; border-radius: 21px;
    font: 700 27px/38px "Playfair Display", Georgia, serif; color: var(--text);
    border: 2px solid var(--accent-line); background: transparent;
  }
  .choice-yes { background: var(--accent); border-color: var(--accent); margin-left: -16px; }

  .remember {
    position: absolute; top: 363px; left: 0; right: 0;
    display: flex; align-items: center; justify-content: center; gap: 6px;
    font-size: 17px;
  }
  .remember-box { width: 16px; height: 16px; border-radius: 3px; background: var(--text); }
</style>
</head>
<body>
  <main class="page">
    <div class="hero-photo" role="img" aria-label="Photo of an embracing couple, tinted in soft purple"></div>
    <div class="dialog-panel"></div>
    <div class="dialog-frame"></div>
    <section class="dialog">
      <div class="brand"><span class="brand-dot"></span>Velvet Dare</div>
      <h1 class="question">ARE YOU OVER 18 YEARS OF AGE?</h1>
      <div class="choices">
        <button class="choice choice-yes">Yes</button>
        <button class="choice choice-no">No</button>
      </div>
      <label class="remember"><span class="remember-box"></span>Remember Me</label>
    </section>
  </main>
</body>
</html>
```